Tobin's Jewelry Studio Needs a Moving Location Flyer

We need a flyer to inform our customers of our location moving. We will be moving to our city's downtown which is only 1 mile away from our current address. We will be having a moving sale ( Up to 80% off). The sale starts Sept. 8th Our business creates, sells, and repairs fine jewelry. Dimensions are 5"x8"

Target Market(s)

Women ages 25-55

Industry/Entity Type

Jewelry

Colors
85abd2
cfdeed

Requirements
Must have
• Our logo
• Mention of the sale
• Our current address
• 4785 Cresthaven Blvd.
• Dunmore, Ca 94318
• (415)826-3319
Nice to have
• Mention that we're relocating to downtown Dunmore (new location opening Nov. 1st.)

```html
<!DOCTYPE html>
<html lang="en">
<head>
<meta charset="UTF-8">
<title>Tobin's Jewelry Studio – Moving Sale</title>
<link rel="stylesheet" href="https://fonts.googleapis.com/css2?family=Damion&family=Roboto:wght@300;400;500&display=swap">
<style>
  :root {
    --blue: #85abd2;
    --blue-light: #cfdeed;
    --brown: #3b1a10;
    --ink: #111111;
    --paper: #ffffff;
  }
  * { margin: 0; padding: 0; box-sizing: border-box; }
  html, body { width: 750px; height: 1200px; overflow: hidden; background: var(--paper); }
  .flyer {
    position: relative;
    width: 750px;
    height: 1200px;
    overflow: hidden;
    background: var(--paper);
    font-family: "Roboto", Arial, sans-serif;
    color: var(--ink);
  }
  .brand {
    position: absolute;
    top: 118px;
    left: 0;
    width: 750px;
    display: flex;
    align-items: center;
    justify-content: center;
    gap: 18px;
  }
  .brand-dot {
    width: 56px;
    height: 56px;
    border-radius: 50%;
    background: var(--blue-light);
  }
  .brand-name {
    font-weight: 500;
    font-size: 34px;
    color: var(--brown);
    letter-spacing: 0.5px;
  }
  .product-photo {
    position: absolute;
    left: 0;
    top: 390px;
    width: 360px;
    height: 600px;
    background: radial-gradient(ellipse at 55% 60%, #e4e6ea 0%, #f3f4f6 45%, #ffffff 75%);
  }
  .headline {
    position: absolute;
    top: 225px;
    left: 0;
    width: 750px;
    text-align: center;
    font-family: "Damion", cursive;
    font-size: 128px;
    line-height: 1;
    color: var(--blue);
  }
  .discount {
    position: absolute;
    top: 396px;
    left: 0;
    width: 760px;
    text-align: center;
    font-size: 39px;
    font-weight: 400;
  }
  .start-badge {
    position: absolute;
    left: 500px;
    top: 440px;
    width: 196px;
    height: 196px;
    border-radius: 50%;
    background: var(--blue);
    color: var(--paper);
    display: flex;
    flex-direction: column;
    justify-content: center;
    align-items: center;
    font-size: 29px;
    line-height: 1.3;
    font-weight: 400;
  }
  .location {
    position: absolute;
    right: 38px;
    top: 736px;
    text-align: right;
    font-size: 25px;
    line-height: 1.1;
  }
  .location-title { font-weight: 500; font-size: 25px; }
  .location-phone { color: var(--blue); font-size: 33px; font-weight: 300; margin-top: 4px; }
  .relocation {
    position: absolute;
    right: 38px;
    top: 914px;
    text-align: right;
    font-size: 25px;
    font-weight: 300;
    line-height: 1.2;
  }
  .relocation-date { color: var(--blue); font-size: 32px; }
  .services-band {
    position: absolute;
    left: -120px;
    top: 1016px;
    width: 990px;
    height: 400px;
    border-radius: 50%;
    background: var(--blue-light);
  }
  .services {
    position: absolute;
    top: 1090px;
    left: 0;
    width: 750px;
    text-align: center;
    font-size: 21px;
    font-weight: 300;
    line-height: 1.5;
  }
</style>
</head>
<body>
  <main class="flyer">
    <header class="brand">
      <span class="brand-dot"></span>
      <span class="brand-name">tobin's jewelry studio</span>
    </header>

    <div class="product-photo" role="img" aria-label="Photo of a silver diamond halo pendant necklace on a chain"></div>

    <h1 class="headline">Moving Sale</h1>
    <p class="discount">(Up to 80% off)</p>

    <div class="start-badge"><span>Starts</span><span>Sept 8</span></div>

    <section class="location">
      <p class="location-title">Current Location</p>
      <p>4785 Cresthaven Blvd</p>
      <p>Dunmore, Ca 94318</p>
      <p class="location-phone">415.826.3319</p>
    </section>

    <section class="relocation">
      <p>We’re relocating to downtown Dunmore</p>
      <p class="relocation-date">Grand Opening Nov 1</p>
    </section>

    <div class="services-band"></div>
    <footer class="services">
      <p>Full Service Jewelry Custom Designing &amp; Fabrication</p>
      <p>Jewelry Repair | Watch Repair | Trade-Ins | Appraisals</p>
    </footer>
  </main>
</body>
</html>
```